Brightfield Optics seeks updated contemporary business card

Brightfield Optics utilizes advanced technology and we take pride in the modern look and feel of our practice. We like our current card, but it's been four years so it is time for an update.

Target Market(s)

Females 25-45 make the most health care decisions for their family.

Contact Information for Business Card

Clean front. Back with info and with empty space for appointment time or other small note

Requirements
Must have
• Logo
Ridge Marketvale, 28413 E Larkspur Ave
Cedar Terrace Marketvale, 4638 S Dunmore Rd
Call or text: 509-342-1968
email: hello@brightfieldoptics.example
brightfieldoptics.example
Dr Tobias Werring & Associates

```html
<!DOCTYPE html>
<html lang="en">
<head>
<meta charset="utf-8">
<title>Brightfield Optics – Business Card</title>
<link rel="stylesheet" href="https://fonts.googleapis.com/css2?family=Montserrat:wght@600;700&family=Open+Sans:wght@400;600&display=swap">
<style>
  :root {
    --backdrop: #939393;
    --card-white: #ffffff;
    --brand-blue: #0a82c0;
    --brand-navy: #2a5587;
    --name-navy: #2d4a7c;
    --text-light: #ffffff;
    --card-shadow: rgba(0, 0, 0, 0.45);
  }
  * { margin: 0; padding: 0; box-sizing: border-box; }
  html, body {
    width: 1200px;
    height: 492px;
    overflow: hidden;
    background: var(--backdrop);
  }
  .canvas {
    position: relative;
    width: 1200px;
    height: 492px;
  }
  .card {
    position: absolute;
    top: 115px;
    width: 447px;
    height: 255px;
    overflow: hidden;
    box-shadow: 6px 8px 10px var(--card-shadow);
  }
  .card-front {
    left: 105px;
    background: var(--card-white);
    display: flex;
    align-items: center;
    justify-content: center;
  }
  .card-back {
    left: 621px;
    background: var(--brand-blue);
  }
  .brand {
    display: flex;
    align-items: center;
    gap: 8px;
    font-family: "Montserrat", sans-serif;
    font-weight: 700;
    color: var(--name-navy);
    text-transform: uppercase;
    white-space: nowrap;
  }
  .brand-dot {
    border-radius: 50%;
    background: var(--brand-blue);
    flex: none;
  }
  .card-front .brand { font-size: 22px; margin-top: 6px; }
  .card-front .brand-dot { width: 16px; height: 16px; }
  .back-shapes {
    position: absolute;
    inset: 0;
  }
  .card-back .brand {
    position: absolute;
    left: 14px;
    top: 132px;
    font-size: 11px;
    gap: 5px;
  }
  .card-back .brand-dot { width: 8px; height: 8px; }
  .practitioner {
    position: absolute;
    right: 31px;
    top: 38px;
    text-align: right;
    font-family: "Montserrat", sans-serif;
    font-weight: 600;
    font-size: 20px;
    line-height: 28px;
    color: var(--text-light);
  }
  .contact {
    position: absolute;
    right: 31px;
    top: 130px;
    list-style: none;
    text-align: right;
    font-family: "Open Sans", sans-serif;
    font-size: 11px;
    letter-spacing: -0.15px;
    white-space: nowrap;
    color: var(--text-light);
  }
  .contact li { height: 19.5px; line-height: 19.5px; }
  .contact li.address { height: 21.5px; line-height: 21.5px; }
</style>
</head>
<body>
<main class="canvas">
  <section class="card card-front" aria-label="Card front">
    <div class="brand"><span class="brand-dot"></span>Brightfield Optics</div>
  </section>

  <section class="card card-back" aria-label="Card back">
    <svg class="back-shapes" width="447" height="255" viewBox="0 0 447 255" aria-hidden="true">
      <circle cx="35" cy="122" r="152" fill="var(--brand-navy)"/>
      <circle cx="35" cy="122" r="145" fill="var(--card-white)"/>
    </svg>
    <div class="brand"><span class="brand-dot"></span>Brightfield Optics</div>
    <h1 class="practitioner">Dr TOBIAS werring<br>&amp; associates</h1>
    <ul class="contact">
      <li>brightfieldoptics.example</li>
      <li>hello@brightfieldoptics.example</li>
      <li>509-342-1968</li>
      <li class="address">Cedar Terrace Marketvale, 4638 S Dunmore Rd</li>
      <li class="address">Ridge Marketvale, 28413 E Larkspur Ave</li>
    </ul>
  </section>
</main>
</body>
</html>
```